Rise Forward: Leave Behind Old Patterns, Quit Drifting Through Days, Begin Shaping each Morning

Good day! I am excited to work again with you, amazing designers! This time I am looking for the cover design of my book.
Dimensions 6” x 9”
The book name is as my name project. I love simplicity, but yet that is impactful. I love colours, I don't have a specific colour in mind, but I like the mustard colour as the one in the logo of my company. I am open to ideas! I have attached some cover samples that I like so that it gives a better idea of what I have on mind.
I am looking for something that looks professional, yet, not super serious, that it's approachable to people. Something that calls their attention at first glance.
I am working with my editor and my interior designer as well to finalize this part of the book. I will be working with the person that I select for the book design to finalize it.
About the book, here a passage of an unedited version of the introduction for guidance :
My intention is to take you on a journey to help you to understand what is going on in your mind so that you get out from anything that is holding you back in your life. My intention is to guide you to start fully living and experiencing a life that your mind even have yet conceived. To experience a life where you live fearless and without suffering. Living your life where you are the navigator and the creator of how you are experiencing it and you are living in a world of possibilities where there are no limitations.
For it, we will start to understand more about the mind and about the brain. I am not a neuroscientist and neither I consider my self an expert in the workings of the brain, what I know is the result of my fascination about our brain. This curiosity and the part of me that likes to understand how things work took me to read, research and learn about how our brain works and how its intrinsic mechanisms are subconsciously influencing and limiting us. I encourage you to stay on this part, it can be a bit technical, but understanding how it works will empower you not to allow your mind to dictate the way you approach your life and to live on autopilot.
We will continue to describe how you have been programmed throughout your life, putting you inside a box limited by your subconscious beliefs and ideas about the world. In this part, we will also discuss what ego is, how it is subconsciously limiting you and how the ways of when ego manifests itself are limiting you and making you suffer. Now that you know how you have been enclosed in your mind for all your life, we will move to discuss how you can get out of it. You will learn how to master your emotions to eliminate your suffering and not allow them to control the direction of your life and use them as a mechanism to get out from your programed mind. We continue to discuss how to leverage the power of your mind and harness your power of choice. Finally, I invite you to see yourself as a holistic being so that you start truly living and take control over the direction of your life, by nourishing and taking care of all those aspects of you utilizing their wisdom and synergy to achieve higher connection within yourself, your soul and live your life in a higher level of consciousness with peace, flow, love and purpose.

```html
<!DOCTYPE html>
<html lang="en">
<head>
<meta charset="utf-8">
<title>Rise Forward – Book Cover</title>
<link rel="stylesheet" href="https://fonts.googleapis.com/css2?family=Playfair+Display:wght@900&family=Montserrat:wght@700&display=swap">
<style>
  :root {
    --backdrop: #121010;
    --paper: #ffffff;
    --ink-blue: #1a4f8d;
    --mustard: #fbbf16;
    --band-text: #ffffff;
  }
  html, body {
    margin: 0;
    padding: 0;
    width: 843px;
    height: 1200px;
    overflow: hidden;
    background: var(--backdrop);
  }
  .cover-art { display: block; width: 843px; height: 1200px; }
  .backdrop { fill: var(--backdrop); }
  .cover-sheet { fill: var(--paper); }
  .title-word {
    font-family: "Playfair Display", "Times New Roman", serif;
    font-weight: 900;
    fill: var(--ink-blue);
  }
  .band-mustard { fill: var(--mustard); }
  .band-blue { fill: var(--ink-blue); }
  .band-text {
    font-family: "Montserrat", Arial, sans-serif;
    font-weight: 700;
    fill: var(--band-text);
  }
  .illustration-area { fill: url(#bulbTones); }
  .author-name {
    font-family: "Montserrat", Arial, sans-serif;
    font-weight: 700;
    fill: var(--ink-blue);
  }
</style>
</head>
<body>
<svg class="cover-art" viewBox="0 0 843 1200" xmlns="http://www.w3.org/2000/svg">
  <defs>
    <linearGradient id="bulbTones" x1="0" y1="0" x2="0" y2="1">
      <stop offset="0" stop-color="#f3c63a"/>
      <stop offset="1" stop-color="#1a4f8d"/>
    </linearGradient>
  </defs>
  <rect class="backdrop" x="0" y="0" width="843" height="1200"/>
  <rect class="cover-sheet" x="103" y="113" width="656" height="975"/>

  <text class="title-word" x="156" y="370" font-size="170" textLength="517" lengthAdjust="spacingAndGlyphs">RISE</text>
  <text class="title-word" x="154" y="522" font-size="86" textLength="386" lengthAdjust="spacingAndGlyphs">FORWARD</text>

  <rect class="illustration-area" role="img" aria-label="Light bulb illustration with a brain inside" x="556" y="398" width="106" height="158" rx="14"/>

  <polygon class="band-mustard" points="126,535 739,552 733,633 131,620"/>
  <text class="band-text" x="432" y="599" font-size="34" text-anchor="middle" textLength="570" lengthAdjust="spacingAndGlyphs">LEAVE BEHIND OLD PATTERNS</text>

  <polygon class="band-mustard" points="558,672 676,669 672,745 561,742"/>
  <text class="band-text" x="620" y="720" font-size="32" text-anchor="middle">AND</text>

  <polygon class="band-blue" points="183,645 577,640 571,767 190,762"/>
  <text class="band-text" x="380" y="697" font-size="35" text-anchor="middle" textLength="320" lengthAdjust="spacingAndGlyphs">QUIT DRIFTING</text>
  <text class="band-text" x="380" y="745" font-size="35" text-anchor="middle" textLength="330" lengthAdjust="spacingAndGlyphs">THROUGH DAYS</text>

  <polygon class="band-mustard" points="165,775 659,778 689,915 190,902"/>
  <text class="band-text" x="420" y="834" font-size="35" text-anchor="middle" textLength="400" lengthAdjust="spacingAndGlyphs">BEGIN SHAPING</text>
  <text class="band-text" x="420" y="884" font-size="35" text-anchor="middle" textLength="300" lengthAdjust="spacingAndGlyphs">EACH MORNING</text>

  <text class="author-name" x="431" y="1028" font-size="42" text-anchor="middle" textLength="490" lengthAdjust="spacingAndGlyphs">MARISOL QUINTERO</text>
</svg>
</body>
</html>
```